URGENT Conference Banner ad to attract a crowd!

I need please in my brand colours 2 x static ads with this copy please:
Have an online business?
Make your customers stick!
It really needs to stand out but not be offensive.
I would like to see blue background on white font and then the reverse. on the white one, it needs a thin blue border around it.
I need it in static: 300x250 and 300x600.
on this one - 300x600. please add a circle saying register now!
Please see examples of other messages I have done. I need this URGENTLY pelase :)
Target Market(s)
http://www.tradefairvaltrona.com.au/en/home/
Industry/Entity Type
Business
Font styles to use
Other font styles liked:
- roboto font
Requirements
Must have
- Use this blue:
- 00b6ce
- roboto font
Nice to have
- look and feel like my banners supplied

```html
<!DOCTYPE html>
<html lang="en">
<head>
<meta charset="utf-8">
<title>Valtrona Trade Fair – Banner Ads</title>
<link rel="stylesheet" href="https://fonts.googleapis.com/css2?family=Roboto:wght@300;500;700&display=swap">
<style>
  :root {
    --brand-blue: #00b6ce;
    --brand-blue-dark: #0a8fb8;
    --badge-blue: #1e9ad6;
    --white: #ffffff;
    --stage: #ececec;
    --apple-red: #c8202a;
    --apple-caramel: #8a4a1c;
  }
  * { box-sizing: border-box; margin: 0; padding: 0; }
  html, body {
    width: 1200px;
    height: 900px;
    overflow: hidden;
  }
  body {
    background: var(--stage);
    font-family: "Roboto", Arial, sans-serif;
    color: var(--white);
    position: relative;
  }
  .banner {
    position: absolute;
    background: var(--brand-blue);
    overflow: hidden;
  }
  .banner--medium { left: 270px; top: 332px; width: 351px; height: 293px; }
  .banner--tall { left: 679px; top: 127px; width: 351px; height: 703px; }

  .brand { position: absolute; font-weight: 300; line-height: 1; }
  .brand__name { display: block; letter-spacing: 0.5px; }
  .brand__tag { display: block; text-align: right; }

  .banner--medium .brand { left: 16px; top: 6px; width: 320px; }
  .banner--medium .brand__name { font-size: 52px; }
  .banner--medium .brand__tag { font-size: 22px; margin-top: 2px; }

  .banner--tall .brand { left: 14px; top: 24px; width: 320px; }
  .banner--tall .brand__name { font-size: 56px; }
  .banner--tall .brand__tag { font-size: 23px; margin-top: 2px; }

  .headline { position: absolute; left: 0; width: 100%; text-align: center; font-weight: 700; }
  .headline__question, .headline__hook { display: block; }

  .banner--medium .headline { top: 88px; }
  .banner--medium .headline__question { font-size: 23px; line-height: 28px; }
  .banner--medium .headline__hook { font-size: 23px; line-height: 28px; }

  .banner--tall .headline { top: 318px; }
  .banner--tall .headline__question { font-size: 40px; line-height: 64px; letter-spacing: 0.5px; }
  .banner--tall .headline__hook { font-size: 34px; line-height: 50px; margin-top: 4px; }

  .product-photo {
    position: absolute;
    border-radius: 40px 40px 30px 30px;
    background: radial-gradient(ellipse at 55% 65%, var(--apple-red) 0%, var(--apple-caramel) 55%, rgba(138,74,28,0) 75%);
  }
  .banner--medium .product-photo { left: 82px; top: 149px; width: 155px; height: 142px; }
  .banner--tall .product-photo { left: 89px; top: 117px; width: 187px; height: 178px; }

  .register-badge { position: absolute; left: 105px; top: 540px; width: 144px; height: 144px; }
</style>
</head>
<body>

  <section class="banner banner--medium" aria-label="300 by 250 banner">
    <div class="brand">
      <span class="brand__name">valtrona</span>
      <span class="brand__tag">trade fair &amp; expo</span>
    </div>
    <h1 class="headline">
      <span class="headline__question">HAVE AN ONLINE BUSINESS?</span>
      <span class="headline__hook">Make your customers stick!</span>
    </h1>
    <div class="product-photo" role="img" aria-label="Photo of four toffee and caramel candy apples on sticks"></div>
  </section>

  <section class="banner banner--tall" aria-label="300 by 600 banner">
    <div class="brand">
      <span class="brand__name">valtrona</span>
      <span class="brand__tag">trade fair &amp; expo</span>
    </div>
    <div class="product-photo" role="img" aria-label="Photo of four toffee and caramel candy apples on sticks"></div>
    <h2 class="headline">
      <span class="headline__question">HAVE AN ONLINE<br>BUSINESS?</span>
      <span class="headline__hook">Make your customers<br>stick!</span>
    </h2>
    <svg class="register-badge" viewBox="0 0 144 144" role="img" aria-label="Register now">
      <defs>
        <radialGradient id="badgeFill" cx="40%" cy="35%" r="70%">
          <stop offset="0" stop-color="#4fc3ee"/>
          <stop offset="1" stop-color="#1679c4"/>
        </radialGradient>
      </defs>
      <circle cx="74" cy="76" r="66" fill="#0a5f8f" opacity="0.35"/>
      <circle cx="72" cy="72" r="66" fill="url(#badgeFill)"/>
      <circle cx="72" cy="72" r="58" fill="none" stroke="#ffffff" stroke-width="2" stroke-dasharray="3 3"/>
      <g transform="rotate(-10 72 72)" fill="#ffffff" font-family="Roboto, Arial, sans-serif" font-weight="700" text-anchor="middle">
        <text x="72" y="64" font-size="20">REGISTER</text>
        <text x="72" y="98" font-size="34">NOW!</text>
      </g>
    </svg>
  </section>

</body>
</html>
```